Book Cover Design Project

I need a book cover for a book that we will be releasing in the next few months.

It is a business book aimed at small businesses and people who want to escape the 9 - 5 and start their own business.

We want it to look similar to: http://www.tolvanbrook.example/wp-content/uploads/2010/03/fold-up.jpg and also the book designs that I have uploaded images for.

I quite like the grey / charcoal background and the bright lime green colours from the Quiet Harbor logo that I have attached. However, anything bright would be good - I am prepared to be flexible with colours. The books I have attached are a high impact as well - being bright blue with white black font with a really cool font.

The book is titled:

The Lantern Shop Plan

By Dale Vortan

Still thinking of the tagline, for now just use "Start an Online Business in no time at all"

Room for a quote/testimonial on the front of the book at the bottom, and as well on the back.

For the back cover text just use dummy text and my photo that is attached for now as well.

Barcode ISBN on the back at the bottom - price will be $19.95

Needs to be in PSD so we can change the text from our end.

I really want to get a good template made that I can edit the text for as we are still developing the book, but I want to get the book cover done so I can start advertising that it will be arriving soon.

There will probably be alterations that I need help with later down the track so looking to work with someone closely on this, and I will pay you for any extra time down the track..

Sizes will probably be around: I think 20.5cm tall and 14cm wide would be good..

Not sure how thick for the spine, it will depend on how many words get cut off, but as an estimate probably 1.5CM..
Updates

Just added some more detail to the brief.. Please read it carefully.

Target Market(s)

small business owners, professionals who want to start their own business, soon to be entrepreneurs, entrepreneurs

Industry/Entity Type

Advertising

Requirements
Must have
• The Lantern Shop Plan

and Dale Vortan must be prominent.

Tag line should be look cool under the title.

Must be very modern and cool. Needs to catch people's eyes so needs to be really punchy.

Nice to have
• Maybe a clock or stopwatch icon would be cool to add in there so it isn't just plain.. Similar to like how the books have a cool icon with them that I have attached in the uploaded images.
Should not have
• I like simplicity, artistic and very high impact. It really needs to draw you in and catch your eye.

Don't use plain boring fonts. Although I like simplicity slick design is very important - I dont want it to be boring - it has to look high quality and expensive. Therefore do not use fonts like Arial, Times New Roman those really boring fonts that make it look cheap. If I was going to do something like that then I might as well do it myself.

If you want to see the quality of things that I am usually involved with look at the artwork for one of my events that I run called Daybreaker: http://www.daybreaker.example/daybreaker-festival-anthems-ft-loomsparrow-harvest-night-eve-metro-report/

That will give you an idea of what type of quality things that I am involved with, so you need to be up for the task..

```html
<!DOCTYPE html>
<html lang="en">
<head>
<meta charset="utf-8">
<title>The Lantern Shop Plan — Dale Vortan</title>
<link rel="stylesheet" href="https://fonts.googleapis.com/css2?family=Bebas+Neue&family=Questrial&family=Raleway:wght@100;200&display=swap">
<style>
  :root {
    --paper: #ebebeb;
    --paper-shade: #e2e2e2;
    --teal: #3cc3a3;
    --teal-deep: #1c9473;
    --ink: #3a3a3a;
    --ribbon-text: #f2f2f2;
  }
  html, body {
    margin: 0;
    padding: 0;
    width: 819px;
    height: 1200px;
    overflow: hidden;
    background: var(--paper);
  }
  .cover {
    position: relative;
    width: 819px;
    height: 1200px;
    overflow: hidden;
  }
  .cover-art {
    position: absolute;
    inset: 0;
    display: block;
  }
  .backdrop-fill { fill: url(#backdrop-tone); }
  .ribbon-line, .ribbon-band { fill: var(--teal); }
  .ribbon-fold { fill: var(--teal-deep); }
  .author-name {
    font-family: "Questrial", sans-serif;
    font-size: 74px;
    letter-spacing: 4px;
    fill: var(--ribbon-text);
  }
  .title-lead {
    font-family: "Raleway", sans-serif;
    font-weight: 200;
    font-size: 46px;
    letter-spacing: 3px;
    fill: var(--ink);
  }
  .title-hero {
    font-family: "Bebas Neue", sans-serif;
    font-size: 100px;
    fill: none;
    stroke: var(--teal);
    stroke-width: 24px;
    stroke-linejoin: miter;
  }
  .title-mid {
    font-family: "Raleway", sans-serif;
    font-weight: 100;
    font-size: 78px;
    letter-spacing: 6px;
    fill: var(--ink);
  }
  .title-end {
    font-family: "Questrial", sans-serif;
    font-size: 92px;
    letter-spacing: 6px;
    fill: var(--ribbon-text);
  }
  .tagline {
    font-family: "Questrial", sans-serif;
    font-size: 24px;
    fill: var(--teal);
  }
</style>
</head>
<body>
<main class="cover">
  <svg class="cover-art" width="819" height="1200" viewBox="0 0 819 1200" xmlns="http://www.w3.org/2000/svg">
    <defs>
      <linearGradient id="backdrop-tone" x1="0" y1="0" x2="1" y2="1">
        <stop offset="0" stop-color="#eeeeee"/>
        <stop offset="1" stop-color="#e3e3e3"/>
      </linearGradient>
    </defs>

    <rect class="backdrop-fill" x="0" y="0" width="819" height="1200" role="img" aria-label="Soft grey background with a faint pattern of business and time icons"/>

    <g class="author-ribbon">
      <rect class="ribbon-line" x="89" y="47" width="639" height="5"/>
      <polygon class="ribbon-band" points="89,60 728,60 712,103 728,146 89,146 105,103"/>
      <rect class="ribbon-line" x="89" y="153" width="639" height="5"/>
      <text class="author-name" x="409" y="130" text-anchor="middle">DALE VORTAN</text>
    </g>

    <g class="title">
      <text class="title-lead" x="104" y="216">THE</text>
      <g transform="translate(99 780) scale(2.3 7.75)">
        <text class="title-hero" x="0" y="0" textLength="270" lengthAdjust="spacingAndGlyphs" vector-effect="non-scaling-stroke" style="vector-effect: non-scaling-stroke">LANTERN</text>
      </g>
      <text class="title-mid" x="409" y="855" text-anchor="middle">SHOP</text>
    </g>

    <g class="title-ribbon">
      <polygon class="ribbon-band" points="93,945 190,945 190,1047 93,1047 120,996"/>
      <polygon class="ribbon-fold" points="147,1007 190,1007 190,1047"/>
      <polygon class="ribbon-band" points="726,945 629,945 629,1047 726,1047 699,996"/>
      <polygon class="ribbon-fold" points="672,1007 629,1007 629,1047"/>
      <rect class="ribbon-band" x="147" y="907" width="525" height="100"/>
      <text class="title-end" x="409" y="989" text-anchor="middle">PLAN</text>
    </g>

    <text class="tagline" x="409" y="1108" text-anchor="middle" textLength="639" lengthAdjust="spacing">START AN ONLINE BUSINESS IN NO TIME AT ALL!</text>
  </svg>
</main>
</body>
</html>
```